Corwick Habitat Web

We just need an update/re-design of our existing web site that would include our new company logo and some new photo's. Our current web site can be viewed at www.corwickhabitat.com.au. We would require something very similar to what we have at the moment in terms of content it should all be the same.
The web site would basically act more as a portfolio than one that would generate more business.
We are after a very modern and simple design and maybe something where we can upload our own project photo's and project descriptions as we complete them.

Industry/Entity Type

It Company

```html
<!DOCTYPE html>
<html lang="en">
<head>
<meta charset="utf-8">
<title>Corwick Habitat</title>
<link href="https://fonts.googleapis.com/css2?family=Raleway:wght@300;400;600&family=Open+Sans:wght@400;600&display=swap" rel="stylesheet">
<style>
:root{
  --red:#d9444a;
  --ink:#333;
  --muted:#888;
  --line:#e2e2e2;
  --grey-bg:#ececec;
  --dark:#1c1c1c;
  --dark-line:#333;
  --white:#fff;
}
*{box-sizing:border-box;margin:0;padding:0}
html,body{width:1200px;height:2647px;overflow:hidden}
body{position:relative;background:var(--white);font-family:"Open Sans",Arial,sans-serif;color:var(--ink);font-size:11px}
.abs{position:absolute}
.heading{font-family:"Raleway",Arial,sans-serif;font-weight:300;text-transform:uppercase;color:var(--ink)}

/* hero */
.hero{left:0;top:0;width:1200px;height:420px;background:linear-gradient(180deg,#7f9a78 0%,#a9b9a2 40%,#e9ebe6 62%,#3fb3d6 80%,#2e8fb6 100%)}
.hero-title{left:260px;top:186px;font-family:"Raleway",Arial,sans-serif;font-weight:600;color:var(--white);font-size:37px;line-height:40px;text-transform:uppercase}
.hero-dots{left:560px;top:396px;display:flex;gap:8px}
.hero-dots span{width:8px;height:8px;border-radius:50%;background:rgba(255,255,255,.6)}
.hero-dots span:first-child{background:var(--white)}
.brand{left:260px;top:0;width:175px;height:66px;background:var(--red);color:var(--white);font-family:"Raleway",Arial,sans-serif;font-weight:400;font-size:19px;display:flex;align-items:center;justify-content:center}
.main-nav{left:435px;top:0;width:505px;height:48px;background:var(--white);display:flex;align-items:center}
.main-nav .home{width:48px;height:48px;border-right:1px solid var(--line);display:flex;align-items:center;justify-content:center}
.main-nav a{font-size:10px;color:#555;text-decoration:none;text-transform:uppercase;padding:0 20px;letter-spacing:.3px}

/* search */
.search-tabs{left:260px;top:458px;display:flex;gap:4px}
.search-tabs span{font-size:10px;text-transform:uppercase;padding:6px 10px}
.search-tabs .active{background:var(--red);color:var(--white)}
.field{height:26px;border:1px solid #d6d6d6;font-size:9px;color:#999;padding:0 8px;display:flex;align-items:center;justify-content:space-between}
.field i{width:14px;height:24px;border-left:1px solid #d6d6d6;margin-right:-8px;display:flex;align-items:center;justify-content:center;font-style:normal;font-size:7px;color:#555}
.btn-search{background:#2b2b2b;color:var(--white);font-size:10px;text-transform:uppercase;display:flex;align-items:center;justify-content:center;height:26px}

/* grey band */
.grey-band{left:0;top:592px;width:1200px;height:1206px;background:var(--grey-bg)}
.tile{background:linear-gradient(160deg,#f2f2f0,#c9c7c2)}
.tile-caption{position:absolute;left:0;right:0;bottom:0;background:rgba(20,20,20,.85);color:var(--white);font-family:"Raleway",Arial,sans-serif;font-size:14px;text-transform:uppercase;padding:0 14px;display:flex;align-items:center}
.progress{left:260px;top:979px;width:680px;height:9px;background:#d6d6d6}
.progress span{display:block;width:338px;height:9px;background:var(--red)}
.rule{left:260px;top:1019px;width:680px;height:1px;background:#d9d9d9}
.filters{left:270px;top:1106px;display:flex;gap:30px;font-size:9px;color:#aaa;text-transform:uppercase}
.view-toggle{left:888px;top:1104px;display:flex;gap:6px}
.view-toggle span{width:11px;height:11px;border:2px solid #bbb}
.view-toggle span.on{border-color:#555}

.card{width:216px;height:306px;background:var(--white)}
.card .photo{height:130px;background:linear-gradient(160deg,#f4f4f4,#a9a7a2);position:relative}
.card .price{position:absolute;left:0;bottom:0;background:var(--red);color:var(--white);font-size:10px;padding:5px 9px;font-weight:600}
.card h3{font-family:"Raleway",Arial,sans-serif;font-weight:400;font-size:15px;text-transform:uppercase;padding:18px 14px 12px}
.card dl{padding:0 14px}
.card dl div{display:flex;justify-content:space-between;font-size:9px;color:#777;border-top:1px solid var(--line);padding:7px 0}

/* agents */
.agent{width:330px;height:163px;border:1px solid var(--line);background:var(--white)}
.agent .portrait{position:absolute;left:15px;top:15px;width:132px;height:132px;background:linear-gradient(180deg,#b9c7d3,#6b7a88)}
.agent .info{position:absolute;left:165px;top:18px;width:150px;font-size:9px;line-height:14px;color:#777}
.agent .role{font-size:8px;color:#aaa}
.agent h4{font-size:11px;color:var(--ink);text-transform:uppercase;font-weight:600;margin:2px 0 8px}
.agent .mail{color:var(--red)}

/* info strip */
.col-title{font-size:18px}
.col-text{font-size:9px;line-height:15px;color:#777;width:200px}
.btn-dark{background:#2b2b2b;color:var(--white);font-size:8px;text-transform:uppercase;padding:7px 12px}
.post{display:flex;gap:12px;width:216px}
.post .thumb{width:34px;height:34px;background:#d7c8c0;flex:none}
.post b{font-size:9px;color:var(--ink);font-weight:600;display:block}
.post small{font-size:8px;color:#999}

/* footer */
.footer{left:0;top:2327px;width:1200px;height:320px;background:var(--dark)}
.footer .col-title{color:#ddd}
.footer .col-text{color:#888}
.links{font-size:9px;color:#888;line-height:15px}
.subscribe{width:216px;height:24px;background:var(--white);font-size:8px;color:#999;display:flex;align-items:center;justify-content:space-between;padding:0 8px}
.foot-rule{left:260px;top:2562px;width:680px;height:1px;background:var(--dark-line)}
.copyright{left:260px;top:2582px;font-size:8px;color:#777;line-height:13px}
.copyright span{color:var(--red)}
.social{left:850px;top:2584px;display:flex;gap:12px}
.social span{width:12px;height:12px;background:#777}
</style>
</head>
<body>

<!-- hero -->
<div class="abs hero" role="img" aria-label="Photograph of a white villa with a turquoise pool and garden"></div>
<div class="abs brand">Corwick Habitat</div>
<nav class="abs main-nav">
  <div class="home"><svg width="12" height="11" viewBox="0 0 12 11"><path d="M6 0L0 5h2v6h3V7h2v4h3V5h2z" fill="#444"/></svg></div>
  <a>Recent Projects</a><a>Our Services</a><a>About</a><a>Contact Us</a>
</nav>
<h1 class="abs hero-title">27 Alder Crescent<br>Fernvale</h1>
<div class="abs hero-dots"><span></span><span></span><span></span><span></span><span></span></div>

<!-- search -->
<div class="abs search-tabs"><span class="active">For Sale</span><span>For Rent</span></div>
<div class="abs field" style="left:260px;top:507px;width:331px">Keyword for Real Property...</div>
<div class="abs field" style="left:609px;top:507px;width:157px">Bedrooms<i>▼</i></div>
<div class="abs field" style="left:787px;top:507px;width:153px">Bathrooms<i>▼</i></div>
<div class="abs field" style="left:260px;top:541px;width:159px">Min Price<i>▼</i></div>
<div class="abs field" style="left:437px;top:541px;width:154px">Max Price<i>▼</i></div>
<div class="abs field" style="left:609px;top:541px;width:157px">Property Type<i>▼</i></div>
<div class="abs btn-search" style="left:783px;top:541px;width:157px">Search</div>

<!-- featured & properties -->
<div class="abs grey-band"></div>
<div class="abs tile" style="left:260px;top:622px;width:331px;height:333px" role="img" aria-label="Photograph of a bright white kitchen interior"><div class="tile-caption" style="height:55px;font-size:17px">1060 Marlow Walk</div></div>
<div class="abs tile" style="left:609px;top:622px;width:157px;height:159px" role="img" aria-label="Photograph of a modern dining room"><div class="tile-caption" style="height:53px">2170 Kestrel Rd</div></div>
<div class="abs tile" style="left:781px;top:622px;width:159px;height:159px" role="img" aria-label="Photograph of an open plan living room"><div class="tile-caption" style="height:53px">2170 Kestrel Rd</div></div>
<div class="abs tile" style="left:609px;top:794px;width:157px;height:161px" role="img" aria-label="Photograph of a bedroom with large windows"><div class="tile-caption" style="height:53px">2170 Kestrel Rd</div></div>
<div class="abs tile" style="left:781px;top:794px;width:159px;height:161px" role="img" aria-label="Photograph of a terrace overlooking the coast"><div class="tile-caption" style="height:53px">2170 Kestrel Rd</div></div>
<div class="abs progress"><span></span></div>
<div class="abs rule"></div>

<h2 class="abs heading" style="left:260px;top:1042px;font-size:26px">Properties</h2>
<div class="abs filters"><span>All</span><span>House</span><span>Office</span><span>Apartment</span><span>Residential</span></div>
<div class="abs view-toggle"><span></span><span class="on"></span><span></span></div>

<article class="abs card" style="left:260px;top:1154px">
  <div class="photo" role="img" aria-label="Photograph of a kitchen with island bench"><span class="price">$356,000</span></div>
  <h3>1076 Marlow Walk</h3>
  <dl><div><dt>Bathrooms</dt><dd>1</dd></div><div><dt>Bedrooms</dt><dd>1</dd></div><div><dt>Square Footage</dt><dd>3250 sqft</dd></div><div><dt>Type</dt><dd>residential</dd></div></dl>
</article>
<article class="abs card" style="left:492px;top:1154px">
  <div class="photo" role="img" aria-label="Photograph of a loft kitchen with timber beams"><span class="price">$356,000</span></div>
  <h3>4101 Bayline Shore</h3>
  <dl><div><dt>Bathrooms</dt><dd>1</dd></div><div><dt>Bedrooms</dt><dd>1</dd></div><div><dt>Square Footage</dt><dd>3250 sqft</dd></div><div><dt>Type</dt><dd>residential</dd></div></dl>
</article>
<article class="abs card" style="left:724px;top:1154px">
  <div class="photo" role="img" aria-label="Photograph of a white minimalist kitchen"><span class="price">$356,000</span></div>
  <h3>3600 Cedar Row</h3>
  <dl><div><dt>Bathrooms</dt><dd>1</dd></div><div><dt>Bedrooms</dt><dd>1</dd></div><div><dt>Square Footage</dt><dd>3250 sqft</dd></div><div><dt>Type</dt><dd>residential</dd></div></dl>
</article>
<article class="abs card" style="left:260px;top:1471px">
  <div class="photo" role="img" aria-label="Photograph of a kitchen with bar stools"><span class="price">$356,000</span></div>
  <h3>1065 Marlow Walk</h3>
  <dl><div><dt>Bathrooms</dt><dd>1</dd></div><div><dt>Bedrooms</dt><dd>1</dd></div><div><dt>Square Footage</dt><dd>3250 sqft</dd></div><div><dt>Type</dt><dd>residential</dd></div></dl>
</article>
<article class="abs card" style="left:492px;top:1471px">
  <div class="photo" role="img" aria-label="Photograph of a modern living space"><span class="price">$356,000</span></div>
  <h3>2170 Kestrel Rd</h3>
  <dl><div><dt>Bathrooms</dt><dd>1</dd></div><div><dt>Bedrooms</dt><dd>1</dd></div><div><dt>Square Footage</dt><dd>3250 sqft</dd></div><div><dt>Type</dt><dd>residential</dd></div></dl>
</article>
<article class="abs card" style="left:724px;top:1471px">
  <div class="photo" role="img" aria-label="Photograph of a contemporary kitchen"><span class="price">$356,000</span></div>
  <h3>3600 Cedar Row</h3>
  <dl><div><dt>Bathrooms</dt><dd>1</dd></div><div><dt>Bedrooms</dt><dd>1</dd></div><div><dt>Square Footage</dt><dd>3250 sqft</dd></div><div><dt>Type</dt><dd>residential</dd></div></dl>
</article>

<!-- agents -->
<h2 class="abs heading" style="left:260px;top:1825px;font-size:26px">Our Agents</h2>
<div class="abs agent" style="left:260px;top:1882px">
  <div class="portrait" role="img" aria-label="Portrait photograph of an agent in a suit"></div>
  <div class="info"><div class="role">Agent</div><h4>Dale Hartwell</h4><p>Our agent guides every buyer through each step of the sale with care, clear advice and a calm approach.</p><p style="margin-top:6px">Call: 014.220.318<br>Mail: <span class="mail">dhartwell@mailbox.com</span></p></div>
</div>
<div class="abs agent" style="left:610px;top:1882px">
  <div class="portrait" style="background:linear-gradient(180deg,#c8b8a8,#6a5a50)" role="img" aria-label="Portrait photograph of an agent in business attire"></div>
  <div class="info"><div class="role">Agent</div><h4>Mara Ellison</h4><p>Our agent guides every buyer through each step of the sale with care, clear advice and a calm approach.</p><p style="margin-top:6px">Call: 014.220.319<br>Mail: <span class="mail">mellison@mailbox.com</span></p></div>
</div>

<!-- info strip -->
<h3 class="abs heading col-title" style="left:260px;top:2122px">About Me</h3>
<div class="abs col-text" style="left:260px;top:2155px">Fresh homes, crafted rooms and quiet spaces designed with care for the way families live today.<br><br>Simple plans, warm light and honest materials, built to last for years.</div>
<div class="abs btn-dark" style="left:260px;top:2262px">More Info</div>

<h3 class="abs heading col-title" style="left:492px;top:2122px">Twitter</h3>
<div class="abs col-text" style="left:492px;top:2155px">Good morning ... wherever you are today! All of us at Corwick Habitat wish you a pleasant day.<br><span style="color:#aaa">13 hours ago</span></div>
<div class="abs col-text" style="left:492px;top:2214px;display:flex;align-items:center;gap:6px"><span style="width:8px;height:8px;background:#3aa7d8;display:inline-block"></span>Follow @corwickhabitat</div>

<h3 class="abs heading col-title" style="left:724px;top:2122px">Blog</h3>
<div class="abs post" style="left:724px;top:2168px"><div class="thumb" role="img" aria-label="Small blog thumbnail"></div><div><b>Fresh ideas for a bright open kitchen</b><small>By Neil Brandt</small></div></div>
<div class="abs post" style="left:724px;top:2236px"><div class="thumb" role="img" aria-label="Small blog thumbnail"></div><div><b>Fresh ideas for a bright open kitchen</b><small>By Neil Brandt</small></div></div>

<!-- footer -->
<footer class="abs footer"></footer>
<h3 class="abs heading col-title" style="left:260px;top:2364px;color:#ddd">Contact Detail</h3>
<div class="abs col-text" style="left:260px;top:2400px;color:#888">Our team is happy to help with any question about our homes, projects and services.<br><br>Phone: 014.220.318<br>Fax: 014.220.320<br>hello@corwickhabitat.com.au</div>
<h3 class="abs heading col-title" style="left:492px;top:2364px;color:#ddd">Useful Links</h3>
<div class="abs links" style="left:492px;top:2400px">Help and FAQs<br>Home Price<br>Market View<br>Free Credit Report<br>Terms and Conditions<br>Privacy Policy<br>Community Guidelines</div>
<h3 class="abs heading col-title" style="left:724px;top:2364px;color:#ddd">Don't Miss Out</h3>
<div class="abs col-text" style="left:724px;top:2400px;color:#888">Join our mailing list for new projects, open homes and design news straight to your inbox.</div>
<div class="abs subscribe" style="left:724px;top:2470px">Enter your email here...<span style="color:#333">›</span></div>
<div class="abs foot-rule"></div>
<div class="abs copyright">Copyright © 2013 Corwick Habitat. Designed by <span>Corwick Habitat</span><br>All rights reserved.</div>
<div class="abs social"><span></span><span></span><span></span><span></span><span></span><span></span></div>

</body>
</html>
```